Business cards Marta Kessel Sport & Events

I need new business cards to match my new logo design for my company called "Marta Kessel Sport & Events". I'm based in Germany.
With my company, I offer different services in the context of sport.

Marta Kessel owner

Marta Kessel Sports & Events
Birkenfelder Weg 12
D-63118 Offenbach

+49 69 / 31 52 94 07
info@marta-kessel.example
www.marta-kessel.example

Contact Information for Business Card

Marta Kessel Inhaberin Marta Kessel Sport & Events Birkenfelder Weg 12 D-63118 Offenbach +49 69 / 31 52 94 07 info@marta-kessel.example www.marta-kessel.example

Requirements
Must have
• Logo | Double sided business card

```html
<!DOCTYPE html>
<html lang="de">
<head>
<meta charset="utf-8">
<title>Marta Kessel Sport &amp; Events – Visitenkarten</title>
<link href="https://fonts.googleapis.com/css2?family=Roboto+Condensed:wght@700&display=swap" rel="stylesheet">
<style>
  :root {
    --backdrop: #262626;
    --card-white: #ffffff;
    --brand-orange: #f9a21c;
    --orange-shade: #f09c1f;
    --ink: #141414;
  }
  * { box-sizing: border-box; margin: 0; padding: 0; }
  html, body { width: 1200px; height: 900px; overflow: hidden; }
  body {
    background: var(--backdrop);
    font-family: "Roboto Condensed", "Arial Narrow", sans-serif;
    font-weight: 700;
    color: var(--ink);
    position: relative;
  }
  .card {
    position: absolute;
    left: 384px;
    width: 430px;
    height: 246px;
    overflow: hidden;
  }
  .card-front { top: 185px; background: var(--card-white); }
  .card-back  { top: 468px; background: var(--brand-orange); }

  /* Front: brand name */
  .brand-dot {
    position: absolute;
    left: 71px; top: 85px;
    width: 78px; height: 78px;
    border-radius: 50%;
    background: var(--brand-orange);
  }
  .brand-name {
    position: absolute;
    left: 159px; top: 103px;
    font-size: 20px;
    line-height: 21px;
    letter-spacing: 1.5px;
    text-transform: uppercase;
    color: var(--ink);
  }

  /* Back: faint disc decoration */
  .back-disc {
    position: absolute;
    left: 176px; top: 0;
    width: 244px; height: 244px;
    border-radius: 50%;
    background: var(--orange-shade);
  }
  .holder {
    position: absolute;
    left: 57px; top: 57px;
    font-size: 17px;
    line-height: 22px;
  }
  .contact-list {
    position: absolute;
    left: 57px; top: 112px;
    list-style: none;
    font-size: 16px;
    line-height: 19.5px;
  }
  .contact-item {
    display: flex;
    align-items: flex-start;
  }
  .contact-icon {
    width: 10px; height: 10px;
    margin: 5px 12px 0 1px;
    flex: none;
  }
</style>
</head>
<body>

  <section class="card card-front" aria-label="Vorderseite">
    <div class="brand-dot"></div>
    <p class="brand-name">Marta Kessel<br>Sport &amp; Events</p>
  </section>

  <section class="card card-back" aria-label="Rückseite">
    <div class="back-disc"></div>
    <p class="holder">Marta Kessel Inhaberin</p>
    <ul class="contact-list">
      <li class="contact-item">
        <svg class="contact-icon" viewBox="0 0 10 10"><circle cx="5" cy="5" r="5" fill="#141414"/><path d="M3.2 2.6l1 .9-.5.8c.4.8 1 1.4 1.8 1.8l.8-.5.9 1-.7.7C4.6 7 3 5.4 2.6 3.3z" fill="#f9a21c"/></svg>
        <span>+49 69 / 31 52 94 07</span>
      </li>
      <li class="contact-item">
        <svg class="contact-icon" viewBox="0 0 10 10"><circle cx="5" cy="5" r="5" fill="#141414"/><rect x="2.4" y="3.3" width="5.2" height="3.6" fill="#f9a21c"/><path d="M2.4 3.3L5 5.4 7.6 3.3" stroke="#141414" stroke-width=".7" fill="none"/></svg>
        <span>info@marta-kessel.example</span>
      </li>
      <li class="contact-item">
        <svg class="contact-icon" viewBox="0 0 10 10"><circle cx="5" cy="5" r="5" fill="#141414"/><g stroke="#f9a21c" stroke-width=".7" fill="none"><circle cx="5" cy="5" r="3"/><ellipse cx="5" cy="5" rx="1.2" ry="3"/><path d="M2 5h6"/></g></svg>
        <span>marta-kessel.example</span>
      </li>
      <li class="contact-item">
        <svg class="contact-icon" viewBox="0 0 10 10"><circle cx="5" cy="5" r="5" fill="#141414"/><path d="M5 8.2C3.6 6.6 3 5.6 3 4.4a2 2 0 014 0c0 1.2-.6 2.2-2 3.8z" fill="#f9a21c"/><circle cx="5" cy="4.4" r=".8" fill="#141414"/></svg>
        <span>Birkenfelder Weg 12<br>D-63118 Offenbach</span>
      </li>
    </ul>
  </section>

</body>
</html>
```